E-Waste Recycling Company Business Card

New Electronic Recycling Company based in Long Island, New York called "Baron Rustwell" We take outdated computers, components, electrical wire, circuit breakers, ink cartridges, etc. We look mostly for donated items that we recycle for our customers but will pay for large quantities from businesses. The design should reflect that we are environmentally friendly and our unique Quadra Purge process that ensures all personal data is wiped clean off hard drives. Please use our attached logo
Electrical

```html
<!DOCTYPE html>
<html lang="en">
<head>
<meta charset="utf-8">
<title>Baron Rustwell – Business Card</title>
<link href="https://fonts.googleapis.com/css2?family=Open+Sans:wght@400;600;700&display=swap" rel="stylesheet">
<style>
  :root{
    --stage:#6b6b6b;
    --paper:#ffffff;
    --green:#3fa63a;
    --green-light:#7cc24f;
    --green-dark:#2f9a3a;
    --ink:#222222;
    --silver-a:#d9d9d9;
    --silver-b:#f4f4f4;
    --silver-c:#bdbdbd;
  }
  *{margin:0;padding:0;box-sizing:border-box}
  html,body{width:1200px;height:573px;overflow:hidden}
  body{background:var(--stage);position:relative;font-family:"Open Sans",Arial,sans-serif}
  .card{position:absolute;top:160px;width:425px;height:243px;background:var(--paper);overflow:hidden}
  .card--front{left:149px}
  .card--back{left:634px}

  .brand{position:absolute;display:flex;align-items:center;gap:8px}
  .brand__dot{width:14px;height:14px;border-radius:50%;background:var(--green);flex:none}
  .brand__name{color:var(--green);font-weight:700;font-size:17px;line-height:1.15;width:70px}
  .card--front .brand{left:68px;top:83px}
  .card--back .brand{left:170px;top:102px}

  .person{position:absolute;left:237px;top:69px}
  .person__name{color:var(--green);font-weight:600;font-size:16.5px;line-height:20px}
  .person__role{color:var(--ink);font-size:9.5px;margin-top:1px}

  .contacts{position:absolute;left:237px;top:122px;list-style:none}
  .contacts li{display:flex;align-items:center;height:15px;font-size:9.5px;color:var(--ink)}
  .contacts svg{width:10px;height:10px;margin-right:6px;fill:none;stroke:var(--green);stroke-width:1.4}
  .contacts .icon-phone{fill:var(--green);stroke:none}

  .band{position:absolute;left:0;right:0;height:24px;display:flex;align-items:center}
  .card--front .band{top:201px;background:linear-gradient(90deg,var(--green-dark) 0%,var(--green-light) 68%,var(--silver-a) 78%,var(--silver-b) 88%,var(--silver-c) 100%)}
  .card--back .band{top:204px;justify-content:center;background:linear-gradient(90deg,var(--green-dark),var(--green-light))}
  .band__text{color:#fff;font-size:9.5px}
  .card--front .band__text{margin-left:44px}
  .card--back .band__text{letter-spacing:2.2px;font-weight:600;font-size:9px}
  .band__mark{position:absolute;left:288px;top:-10px;width:40px;text-align:center;color:var(--green);font-weight:700;font-size:7px;line-height:1.1}
</style>
</head>
<body>
  <section class="card card--front">
    <div class="brand">
      <span class="brand__dot"></span>
      <span class="brand__name">Baron Rustwell</span>
    </div>

    <div class="person">
      <p class="person__name">Miles Corwin</p>
      <p class="person__role">Managing Director</p>
    </div>

    <ul class="contacts">
      <li><svg class="icon-phone" viewBox="0 0 10 10"><path d="M2 0.5l1.6 2-1 1.1a5.5 5.5 0 0 0 3.8 3.8l1.1-1 2 1.6-1 1.6C4.5 9.6 0.4 5.5 0.5 1.5z"/></svg>000-000-0000</li>
      <li><svg viewBox="0 0 10 10"><rect x="0.7" y="1.8" width="8.6" height="6.4"/><path d="M0.7 1.8l4.3 3.6 4.3-3.6"/></svg>info@youremail.com</li>
      <li><svg viewBox="0 0 10 10"><circle cx="5" cy="5" r="4.2"/><ellipse cx="5" cy="5" rx="1.8" ry="4.2"/><path d="M0.8 5h8.4"/></svg>www.yourwebsite.com</li>
    </ul>

    <div class="band">
      <span class="band__text">Co. Street, Building City/State,Zip Code</span>
      <span class="band__mark">Baron Rustwell</span>
    </div>
  </section>

  <section class="card card--back">
    <div class="brand">
      <span class="brand__dot"></span>
      <span class="brand__name">Baron Rustwell</span>
    </div>
    <div class="band">
      <span class="band__text">www.yourwebsite.com</span>
    </div>
  </section>
</body>
</html>
```